Health Care Service Company Flyer

Company name: Tall Orchard Studio
Slogan: Find out what you're made of
Website: tallorchardstudio.ca

I need the flyer to contain the company name (will provide logo source file ASAP), the slogan in large font and a "find out more at orchardstudio.ca"

Other important data to include in the flyer is:
Four bullet points with the following information:
*Track performance and fitness results over time
*Develop proprietary exercise and dietary programs based on actionable data
*Track muscle atrophy from injury, as well as muscle gain during rehabilitation
*Reveal imbalances in muscle symmetry and strength, flexibility, and joint mechanics

I also need the following information conveyed somewhere on the flyer:
*Body Fat, Muscle Mass, and Bone Density Measurements
• Over 50 data points generated in each 10 minute scan
*Call XXX-XXX-XXX to book an appointment today

DEXA Body Composition Services.
Get scanned today.

See example of competitor flyers in the images to get an example of the images and information we are trying to convey

Target Market(s)

athletes, fitness enthusiast, crossfit

Industry/Entity Type

Health And Wellness

Colors
33a6d7
acd036

Requirements
Nice to have
• Prefer images be general health and wellness related - in other words, individuals who look healthy, but are not abnormally muscular
Should not have
• Shirtless models, No big muscles,

```html
<!DOCTYPE html>
<html lang="en">
<head>
<meta charset="utf-8">
<title>Tall Orchard Studio – DEXA Body Composition Flyer</title>
<link rel="stylesheet" href="https://fonts.googleapis.com/css2?family=Source+Sans+3:wght@300;400;600;700&display=swap">
<style>
  :root {
    --brand-blue: #1e84c8;
    --brand-blue-light: #33a6d7;
    --brand-blue-deep: #1873b3;
    --brand-green: #8dc63f;
    --brand-green-bright: #acd036;
    --text-grey: #6a6a6a;
    --paper: #ffffff;
    --figure-grey: #d4d4d4;
    --figure-orange: #ee7a22;
  }
  * { box-sizing: border-box; margin: 0; padding: 0; }
  html, body {
    width: 950px; height: 1200px; overflow: hidden;
    background: var(--paper);
    font-family: "Source Sans 3", sans-serif;
  }
  .flyer { position: relative; width: 950px; height: 1200px; background: var(--paper); }

  .masthead {
    position: absolute; left: 0; top: 0; width: 950px; height: 124px;
    display: flex; align-items: center; justify-content: center;
  }
  .company-name {
    font-weight: 700; font-size: 54px; letter-spacing: 2px;
    text-transform: uppercase; color: var(--brand-blue-light);
  }

  .hero {
    position: absolute; left: 0; top: 124px; width: 950px; height: 468px;
    background: var(--brand-blue); overflow: hidden;
  }
  .hero-glow {
    position: absolute; left: 0; top: 0; width: 950px; height: 468px;
  }
  .hero-photo {
    position: absolute; left: 0; top: -20px; width: 580px; height: 488px;
    background: linear-gradient(135deg, #c9c9cb 0%, #b9bec4 35%, #4a9fdc 60%, #2f8fd3 100%);
  }
  .headline {
    position: absolute; right: 40px; top: 126px; text-align: right;
    color: var(--paper); text-transform: uppercase; line-height: 1.18;
  }
  .headline-light { display: block; font-weight: 300; font-size: 44px; }
  .headline-bold { display: block; font-weight: 700; font-size: 44px; letter-spacing: -0.5px; }
  .web-pill {
    position: absolute; left: 533px; top: 252px; width: 389px; height: 41px;
    border-radius: 21px; background: var(--brand-green);
    color: var(--paper); font-size: 24px; font-weight: 400;
    display: flex; align-items: center; justify-content: center;
    box-shadow: 0 2px 4px rgba(0,0,0,0.2);
  }
  .web-pill strong { font-weight: 700; margin-left: 6px; }
  .service-note {
    position: absolute; right: 40px; top: 330px; text-align: right;
    color: var(--paper); font-size: 18px; line-height: 1.5;
  }
  .service-note strong { font-weight: 700; text-transform: uppercase; }

  .benefits { position: absolute; left: 28px; top: 0; width: 660px; }
  .benefit {
    position: absolute; left: 0; width: 660px;
    display: flex; align-items: center;
  }
  .benefit-icon { flex: 0 0 64px; width: 64px; height: 64px; }
  .benefit-text {
    margin-left: 33px; font-size: 26px; line-height: 1.32;
    color: var(--text-grey); font-weight: 400;
  }

  .anatomy-figure {
    position: absolute; left: 710px; top: 642px; width: 172px; height: 378px;
    border-radius: 80px 80px 30px 30px;
    background: linear-gradient(180deg, var(--figure-grey) 0%, var(--figure-orange) 25%, #f3a13a 45%, var(--figure-orange) 60%, var(--figure-grey) 80%);
  }

  .footer-band {
    position: absolute; left: 0; top: 1070px; width: 950px; height: 130px;
    background: var(--brand-blue-deep);
  }
  .call-pill {
    position: absolute; left: 143px; top: 1044px; width: 670px; height: 52px;
    border-radius: 26px; background: var(--brand-green);
    color: var(--paper); font-size: 25px;
    display: flex; align-items: center; justify-content: center; gap: 10px;
    box-shadow: 0 2px 4px rgba(0,0,0,0.2);
  }
  .call-pill .phone-icon { width: 26px; height: 26px; margin-left: 10px; }
  .call-pill strong { font-weight: 700; }
  .measurements {
    position: absolute; left: 0; top: 1106px; width: 950px; text-align: center;
    color: var(--paper); font-size: 30px; font-weight: 600; text-transform: uppercase;
  }
  .measurements .dot { color: var(--brand-green); margin: 0 10px; font-size: 22px; vertical-align: middle; }
  .scan-note {
    position: absolute; left: 0; top: 1148px; width: 950px; text-align: center;
    color: var(--brand-green); font-size: 24px; font-weight: 600;
  }
</style>
</head>
<body>
<main class="flyer">

  <header class="masthead">
    <span class="company-name">Tall Orchard Studio</span>
  </header>

  <section class="hero">
    <svg class="hero-glow" width="950" height="468" viewBox="0 0 950 468" aria-hidden="true">
      <polygon points="560,0 950,0 950,468 470,468" fill="#2590d2"/>
    </svg>
    <div class="hero-photo" role="img" aria-label="Photo of a smiling woman and man jogging together in athletic t-shirts"></div>
    <h1 class="headline">
      <span class="headline-light">Find out what</span>
      <span class="headline-bold">You're made of</span>
    </h1>
    <div class="web-pill">find out more at <strong>orchardstudio.ca</strong></div>
    <p class="service-note">DEXA Body Composition Services.<br><strong>Get scanned today.</strong></p>
  </section>

  <ul class="benefits">
    <li class="benefit" style="top:644px">
      <svg class="benefit-icon" viewBox="0 0 64 64" aria-hidden="true">
        <circle cx="32" cy="32" r="31" fill="var(--brand-green)"/>
        <circle cx="29" cy="29" r="11" fill="none" stroke="var(--brand-blue)" stroke-width="5"/>
        <line x1="37" y1="37" x2="48" y2="48" stroke="var(--brand-blue)" stroke-width="6" stroke-linecap="round"/>
      </svg>
      <span class="benefit-text">Track performance and fitness results over time</span>
    </li>
    <li class="benefit" style="top:722px">
      <svg class="benefit-icon" viewBox="0 0 64 64" aria-hidden="true">
        <circle cx="32" cy="32" r="31" fill="var(--brand-green)"/>
        <rect x="20" y="17" width="24" height="32" rx="2" fill="var(--brand-blue)"/>
        <rect x="27" y="13" width="10" height="7" rx="2" fill="#14598c"/>
        <line x1="24" y1="27" x2="40" y2="27" stroke="#fff" stroke-width="2"/>
        <line x1="24" y1="33" x2="40" y2="33" stroke="#fff" stroke-width="2"/>
        <line x1="24" y1="39" x2="36" y2="39" stroke="#fff" stroke-width="2"/>
      </svg>
      <span class="benefit-text">Develop proprietary exercise and dietary<br>programs based on actionable data</span>
    </li>
    <li class="benefit" style="top:813px">
      <svg class="benefit-icon" viewBox="0 0 64 64" aria-hidden="true">
        <circle cx="32" cy="32" r="31" fill="var(--brand-green)"/>
        <rect x="16" y="24" width="6" height="16" rx="1" fill="var(--brand-blue)"/>
        <rect x="42" y="24" width="6" height="16" rx="1" fill="var(--brand-blue)"/>
        <rect x="11" y="27" width="5" height="10" rx="1" fill="var(--brand-blue)"/>
        <rect x="48" y="27" width="5" height="10" rx="1" fill="var(--brand-blue)"/>
        <rect x="22" y="30" width="20" height="4" fill="var(--brand-blue)"/>
      </svg>
      <span class="benefit-text">Track muscle atrophy from injury, as well as<br>muscle gain during rehabilitation</span>
    </li>
    <li class="benefit" style="top:911px">
      <svg class="benefit-icon" viewBox="0 0 64 64" aria-hidden="true">
        <circle cx="32" cy="32" r="31" fill="var(--brand-green)"/>
        <rect x="18" y="18" width="28" height="34" rx="4" fill="var(--brand-blue)"/>
        <circle cx="32" cy="29" r="7" fill="none" stroke="#fff" stroke-width="2"/>
        <line x1="32" y1="29" x2="35" y2="25" stroke="#fff" stroke-width="2"/>
        <line x1="32" y1="38" x2="32" y2="52" stroke="#fff" stroke-width="2"/>
      </svg>
      <span class="benefit-text">Reveal imbalances in muscle symmetry and<br>strength, flexibility, and joint mechanics</span>
    </li>
  </ul>

  <div class="anatomy-figure" role="img" aria-label="Illustration of a standing human muscle chart with chest, shoulders, abdominals and thighs highlighted in orange"></div>

  <div class="footer-band"></div>
  <div class="call-pill">
    <span>Call</span>
    <svg class="phone-icon" viewBox="0 0 26 26" aria-hidden="true">
      <circle cx="13" cy="13" r="11.5" fill="none" stroke="#fff" stroke-width="2"/>
      <path d="M9 7.5c.6-.4 1.3-.3 1.6.3l1 2c.3.6.1 1.1-.4 1.5l-.6.5c.6 1.5 1.8 2.7 3.3 3.4l.5-.6c.4-.5 1-.6 1.5-.4l2 1c.6.3.7 1 .3 1.6l-.8 1c-.5.6-1.3.8-2 .5-3.3-1.3-5.9-3.9-7.2-7.2-.3-.7-.1-1.5.5-2z" fill="#fff"/>
    </svg>
    <span><strong>XXX-XXX-XXX</strong> to book an appointment today</span>
  </div>
  <p class="measurements">Body Fat<span class="dot">•</span>Muscle Mass<span class="dot">•</span>Bone Density Measurements</p>
  <p class="scan-note">Over 50 data points generated in each 10 minute scan</p>

</main>
</body>
</html>
```